Letterhead - Quarrington Law Group

I receive a fantastic logo from you guys and I'd like to incorporate it into business cards and letterhead. I accidentally approved design No. 32361474 and contacted designer Ravindra, and Ravindra sent me the zip folder for Design No. 32361417, which I very much appreciate.
I'd like to order business cards and letterhead with Design No. 32361417 as soon as possible, but I want to make sure that you incorporate the correct design (attached). I'd also like to provide my information to add (address, phone number, email, fax) but I'm not quite sure how to do it.
The information that I would like on the business cards and letterhead is as follows:
Quarrington Law Group
Theodore K. Quarrington, Esq.
2741 Hollis Avenue, Suite 520
San Francisco, CA 94087
Office: (415) 378-6130
Fax: (415) 746-0183
ted@quarringtonlawgroup-example.com
Thanks in advance for any guidance.
Ted Quarrington
Quarrington Law Group
(415) 831-4497 (cell)

```html
<!DOCTYPE html>
<html lang="en">
<head>
<meta charset="utf-8">
<title>Quarrington Law Group – Letterhead &amp; Business Cards</title>
<link rel="stylesheet" href="https://fonts.googleapis.com/css2?family=Tinos:wght@400;700&family=Montserrat:wght@600&family=Questrial&display=swap">
<style>
  :root {
    --ink: #1b1a19;
    --blue: #1a8ccc;
    --paper: #ffffff;
    --grey-text: #8c8c8c;
    --backdrop: #858585;
  }
  * { box-sizing: border-box; margin: 0; padding: 0; }
  html, body { width: 1155px; height: 1200px; overflow: hidden; background: var(--backdrop); }
  .canvas { position: relative; width: 1155px; height: 1200px; background: var(--backdrop); overflow: hidden; }

  .sheet, .card { position: absolute; background: var(--paper); overflow: hidden; }
  .sheet { left: 114px; top: 101px; width: 705px; height: 998px; }
  .decor { position: absolute; left: 0; top: 0; }

  .wordmark {
    position: absolute; font-family: "Tinos", serif; font-weight: 400;
    color: var(--ink); line-height: 1.05; letter-spacing: 0.5px;
  }
  .sheet .wordmark { left: 48px; top: 62px; font-size: 27px; }

  .contact { position: absolute; font-family: "Tinos", serif; color: #555; list-style: none; }
  .contact li { display: flex; align-items: flex-start; }
  .contact .icon { flex: none; display: block; }
  .sheet .contact { left: 495px; top: 40px; font-size: 11px; line-height: 14px; }
  .sheet .contact li { margin-bottom: 8px; }
  .sheet .contact li:first-child { margin-bottom: 11px; }
  .sheet .contact .icon { width: 15px; height: 15px; margin-right: 5px; }

  .recipient { position: absolute; left: 43px; top: 266px; font-family: "Questrial", sans-serif; color: var(--grey-text); font-size: 13px; line-height: 22px; }
  .recipient h2 { font-family: "Montserrat", sans-serif; font-weight: 600; color: var(--ink); font-size: 21px; line-height: 28px; margin-bottom: 2px; }
  .recipient p + p { margin-top: 0; }
  .recipient .address { line-height: 17px; margin-top: 4px; }

  .body-copy { position: absolute; left: 43px; top: 410px; width: 615px; font-family: "Questrial", sans-serif; color: var(--grey-text); font-size: 15.6px; line-height: 22px; text-align: justify; }
  .body-copy p + p { margin-top: 22px; }

  .sign-off { position: absolute; right: 60px; top: 782px; font-family: "Tinos", serif; font-weight: 700; font-size: 21px; color: var(--ink); }
  .surname { color: var(--blue); }
  .signature { position: absolute; left: 489px; top: 832px; width: 120px; height: 78px; background: linear-gradient(135deg, #f2f2f2, #e4e4e4); border-radius: 4px; }

  .card-front { left: 643px; top: 283px; width: 343px; height: 212px; background: var(--blue); }
  .card-front .wordmark { left: 100px; top: 72px; width: 150px; color: var(--paper); font-size: 22px; text-align: center; }

  .card-back { left: 641px; top: 530px; width: 349px; height: 213px; }
  .card-back .wordmark { left: 30px; top: 85px; font-size: 19px; }
  .holder { position: absolute; left: 190px; top: 40px; font-family: "Tinos", serif; }
  .holder h3 { font-weight: 700; font-size: 15px; color: var(--ink); line-height: 18px; }
  .holder .role { font-size: 8.5px; color: #555; margin-top: 2px; }
  .holder .rule { width: 31px; height: 1px; background: var(--blue); margin-top: 6px; }
  .card-back .contact { left: 190px; top: 90px; font-size: 7px; line-height: 9.5px; }
  .card-back .contact li { margin-bottom: 5px; }
  .card-back .contact li:first-child { margin-bottom: 7px; }
  .card-back .contact .icon { width: 10px; height: 10px; margin-right: 4px; }
</style>
</head>
<body>
<main class="canvas">

  <!-- Letterhead -->
  <section class="sheet" aria-label="Letterhead">
    <svg class="decor" width="705" height="998" viewBox="0 0 705 998" aria-hidden="true">
      <path d="M572,0 Q682,22 705,102 L705,0 Z" fill="var(--blue)"/>
      <path d="M0,796 Q42,985 262,998 L0,998 Z" fill="var(--blue)"/>
      <path d="M0,800 Q42,984 254,998 L0,998 Z" fill="var(--paper)"/>
      <path d="M0,812 Q44,982 232,998 L0,998 Z" fill="var(--ink)"/>
    </svg>

    <div class="wordmark">Quarrington<br>Law Group</div>

    <ul class="contact">
      <li><svg class="icon" viewBox="0 0 16 16"><rect width="16" height="16" rx="2" fill="var(--blue)"/><path d="M8 3a3.2 3.2 0 0 0-3.2 3.2C4.8 8.8 8 13 8 13s3.2-4.2 3.2-6.8A3.2 3.2 0 0 0 8 3zm0 4.5a1.3 1.3 0 1 1 0-2.6 1.3 1.3 0 0 1 0 2.6z" fill="#fff"/></svg>
        <span>Theodore K. Quarrington, Esq.<br>2741 Hollis Avenue, Suite 520<br>San Francisco, CA 94087</span></li>
      <li><svg class="icon" viewBox="0 0 16 16"><rect width="16" height="16" rx="2" fill="var(--ink)"/><path d="M5.2 3.5l1.6 2.2-1 1.1c.6 1.4 1.6 2.4 3 3l1.1-1 2.2 1.6-.8 1.9C7.6 12.2 3.8 8.4 3.6 4.3z" fill="#fff"/></svg>
        <span>(415) 378-6130</span></li>
      <li><svg class="icon" viewBox="0 0 16 16"><rect width="16" height="16" rx="2" fill="var(--ink)"/><rect x="5" y="3" width="6" height="3" fill="#fff"/><rect x="3.5" y="6.5" width="9" height="4.5" rx="1" fill="#fff"/><rect x="5" y="9.5" width="6" height="3.5" fill="#fff" stroke="var(--ink)" stroke-width=".8"/></svg>
        <span>(415) 746-0183</span></li>
      <li><svg class="icon" viewBox="0 0 16 16"><rect width="16" height="16" rx="2" fill="var(--ink)"/><rect x="3" y="4.5" width="10" height="7" fill="#fff"/><path d="M3 4.5l5 4 5-4M3 11.5l3.6-3.6M13 11.5L9.4 7.9" stroke="var(--ink)" stroke-width=".9" fill="none"/></svg>
        <span>ted@quarringtonlawgroup-example.com</span></li>
    </ul>

    <div class="recipient">
      <h2>Mara Ellison</h2>
      <p>0198-372-645</p>
      <p>info@recipientmail-example.com</p>
      <p class="address">4826 Elm Park Rd. Suite<br>214 Dallas, TX 75201</p>
    </div>

    <div class="body-copy">
      <p>Lorem ipsum dolor sit amet, consectetuer adipiscing elit, sed diam nonummy nibh euismod tincidunt ut laoreet dolore magna aliquam erat volutpat. Ut wisi enim ad minim veniam, quis nostrud exerci tation ullamcorper suscipit lobortis nisl ut aliquip ex ea commodo consequat. Duis autem vel eum iriure dolor in hendrerit in vulputate velit esse molestie consequat, vel illum dolore eu feugiat nulla facilisis at vero eros et accumsan et iusto odio dignissim qui blandit praesent luptatum zzril delenit augue duis dolore te feugait nulla facilisi.</p>
      <p>Lorem ipsum dolor sit amet, cons ectetuer adipiscing elit, sed diam nonummy nibh euismod tincidunt ut laoreet dolore magna aliquam erat volutpat. Ut wisi enim ad minim veniam, quis nostrud exerci tation ullamcorper suscipit lobortis nisl ut aliquip ex ea commodo consequat.</p>
      <p>Lorem ipsum dolor sit amet, consectetuer adipiscing elit, sed diam nonummy nibh euismod tincidunt ut laoreet dolore magna aliquam erat</p>
    </div>

    <div class="sign-off">Mr. Ted <span class="surname">Quarrington</span></div>
    <div class="signature" role="img" aria-label="Handwritten signature of Ted Quarrington"></div>
  </section>

  <!-- Business card, front -->
  <section class="card card-front" aria-label="Business card front">
    <svg class="decor" width="343" height="212" viewBox="0 0 343 212" aria-hidden="true">
      <path d="M0,0 L158,0 Q326,8 343,150 L343,212 L0,212 Z" fill="var(--paper)"/>
      <path d="M0,0 L146,0 Q318,12 343,168 L343,212 L0,212 Z" fill="var(--ink)"/>
    </svg>
    <div class="wordmark">Quarrington<br>Law Group</div>
  </section>

  <!-- Business card, back -->
  <section class="card card-back" aria-label="Business card back">
    <svg class="decor" width="349" height="213" viewBox="0 0 349 213" aria-hidden="true">
      <path d="M0,94 Q18,198 138,213 L0,213 Z" fill="var(--blue)"/>
      <path d="M0,98 Q18,196 130,213 L0,213 Z" fill="var(--paper)"/>
      <path d="M0,104 Q20,195 120,213 L0,213 Z" fill="var(--ink)"/>
    </svg>
    <div class="wordmark">Quarrington<br>Law Group</div>

    <div class="holder">
      <h3>Ted <span class="surname">Quarrington</span></h3>
      <p class="role">Managing Director</p>
      <div class="rule"></div>
    </div>

    <ul class="contact">
      <li><svg class="icon" viewBox="0 0 16 16"><rect width="16" height="16" rx="2" fill="var(--blue)"/><path d="M8 3a3.2 3.2 0 0 0-3.2 3.2C4.8 8.8 8 13 8 13s3.2-4.2 3.2-6.8A3.2 3.2 0 0 0 8 3zm0 4.5a1.3 1.3 0 1 1 0-2.6 1.3 1.3 0 0 1 0 2.6z" fill="#fff"/></svg>
        <span>Theodore K. Quarrington, Esq.<br>2741 Hollis Avenue, Suite 520<br>San Francisco, CA 94087</span></li>
      <li><svg class="icon" viewBox="0 0 16 16"><rect width="16" height="16" rx="2" fill="var(--ink)"/><path d="M5.2 3.5l1.6 2.2-1 1.1c.6 1.4 1.6 2.4 3 3l1.1-1 2.2 1.6-.8 1.9C7.6 12.2 3.8 8.4 3.6 4.3z" fill="#fff"/></svg>
        <span>(415) 378-6130</span></li>
      <li><svg class="icon" viewBox="0 0 16 16"><rect width="16" height="16" rx="2" fill="var(--ink)"/><rect x="5" y="3" width="6" height="3" fill="#fff"/><rect x="3.5" y="6.5" width="9" height="4.5" rx="1" fill="#fff"/><rect x="5" y="9.5" width="6" height="3.5" fill="#fff" stroke="var(--ink)" stroke-width=".8"/></svg>
        <span>(415) 746-0183</span></li>
      <li><svg class="icon" viewBox="0 0 16 16"><rect width="16" height="16" rx="2" fill="var(--ink)"/><rect x="3" y="4.5" width="10" height="7" fill="#fff"/><path d="M3 4.5l5 4 5-4M3 11.5l3.6-3.6M13 11.5L9.4 7.9" stroke="var(--ink)" stroke-width=".9" fill="none"/></svg>
        <span>ted@quarringtonlawgroup-example.com</span></li>
    </ul>
  </section>

</main>
</body>
</html>
```